New Graphic Design Project / Email signiture and Letterhead

I would like a new SIMPLE but high end quality modern/heavy industrial design for an email Signiture and letter head that incorporates product photos or illustrations of our products to show our customers our range of products and also show our head office in Perth Western Australia and also our Australian and international reseller locations.
in my present email signature you would see that I have other company logos these companies are old partners of ours but some are no longer so I would like to have the option to add and change them if things change in the future.
for ideas Our main products are as follows
Composite Hose
Convoluted hose
Metal expansion joints
Fabric expansion joints
Rubber Expansion joints
Please see our website for ideas and our product photos.
www.brovantec.com.au
if you need any further information please let me know
i have attached our old email signiture for reference.
Declan

Target Market(s)

Oil and Gas / Mining / Petroleum and Chemical Refineries, high end engineering

Requirements
Must have
• pictures / photos of our core products and our company capabilities to show our existing and new customers what we can do.
in the email signature - links to company face book and LinkedIn, our website
I would like to have spaces for my company partners logos and need the final file to be in a format for me to change and update all details
All so our Font is Conthrax SB
Nice to have
• the email signature, I would like this to have all the required information ( as per attached present email signature ) but also be informative / marketing to show customers what we do if possible.
the letter head can be based from the same but simple with or without product photos

```html
<!DOCTYPE html>
<html lang="en">
<head>
<meta charset="utf-8">
<title>Brovantec – Email Signature and Letterhead</title>
<link rel="stylesheet" href="https://fonts.googleapis.com/css2?family=Orbitron:wght@600;700&family=Open+Sans:wght@400;600&display=swap">
<style>
  :root {
    --navy: #14204d;
    --navy-deep: #0d1638;
    --blue: #1f4fa8;
    --blue-bright: #2b6fd6;
    --sky: #9fc0ea;
    --ink: #3a3f4a;
    --muted: #8a909c;
    --paper: #ffffff;
    --canvas: #f1f2f4;
    --map: #e4e7ec;
  }
  * { box-sizing: border-box; margin: 0; padding: 0; }
  html, body { width: 900px; height: 1200px; overflow: hidden; }
  body {
    background: var(--canvas);
    font-family: "Open Sans", Arial, sans-serif;
    color: var(--ink);
    position: relative;
  }

  /* ---------- Email signature ---------- */
  .signature {
    position: absolute; left: 105px; top: 75px;
    width: 690px; height: 255px;
    background: var(--paper);
    box-shadow: 0 2px 8px rgba(0,0,0,.12);
    overflow: hidden;
  }
  .signature__photo {
    position: absolute; left: 0; top: 0; width: 190px; height: 100%;
    background: linear-gradient(180deg, #2a2458 0%, #4b3c7a 40%, #6a5a8e 60%, #1b1a33 100%);
  }
  .signature__band {
    position: absolute; left: 190px; top: 0; right: 0; height: 66px;
    background: var(--navy);
  }
  .signature__band svg { position: absolute; right: 0; top: 0; }
  .signature__name {
    position: absolute; left: 215px; top: 8px;
    font-family: "Orbitron", "Arial Black", sans-serif; font-weight: 700;
    font-size: 28px; letter-spacing: 1px; color: #fff; text-transform: uppercase;
  }
  .signature__role {
    position: absolute; left: 215px; top: 42px;
    font-size: 13px; color: #dfe6f5;
  }
  .signature__contacts {
    position: absolute; left: 208px; top: 80px; list-style: none;
  }
  .signature__contacts li {
    display: flex; align-items: center; gap: 8px;
    font-size: 10.5px; color: var(--ink); height: 18px;
  }
  .contact-icon {
    width: 13px; height: 13px; border-radius: 50%;
    background: var(--navy); display: inline-flex; align-items: center; justify-content: center;
  }
  .signature__social { position: absolute; left: 208px; top: 158px; display: flex; gap: 7px; }
  .social-dot { width: 13px; height: 13px; border-radius: 50%; background: var(--navy); }
  .signature__map {
    position: absolute; left: 400px; top: 70px; width: 230px; height: 110px;
    background: radial-gradient(ellipse at center, var(--map) 0%, rgba(228,231,236,0) 70%);
  }
  .brand {
    display: flex; align-items: center; gap: 7px;
    font-family: "Orbitron", "Arial Black", sans-serif; font-weight: 700;
    color: var(--navy); text-transform: uppercase; letter-spacing: .5px;
  }
  .brand__dot { border-radius: 50%; border: 3px solid var(--navy); }
  .signature .brand { position: absolute; right: 16px; top: 138px; font-size: 15px; }
  .signature .brand__dot { width: 20px; height: 20px; }
  .signature__disclaimer {
    position: absolute; left: 208px; right: 20px; top: 186px;
    font-size: 8.5px; line-height: 1.5; color: var(--muted);
  }

  /* ---------- Letterhead ---------- */
  .letterhead {
    position: absolute; left: 135px; top: 375px;
    width: 630px; height: 780px;
    background: var(--paper);
    box-shadow: 0 2px 8px rgba(0,0,0,.12);
    overflow: hidden;
  }
  .letterhead__header-band { position: absolute; right: 0; top: 0; }
  .letterhead .brand { position: absolute; left: 30px; top: 30px; font-size: 16px; }
  .letterhead .brand__dot { width: 22px; height: 22px; }
  .letterhead__map {
    position: absolute; left: 250px; top: 380px; width: 370px; height: 330px;
    background: radial-gradient(ellipse at 60% 55%, var(--map) 0%, rgba(228,231,236,.5) 45%, rgba(255,255,255,0) 72%);
  }
  .letterhead__body {
    position: absolute; left: 30px; right: 40px; top: 135px;
    font-size: 8.5px; line-height: 1.55; color: var(--ink);
  }
  .letterhead__body p { margin-bottom: 10px; }
  .letterhead__signoff { margin-top: 14px; }
  .letterhead__social { position: absolute; left: 30px; top: 715px; display: flex; gap: 8px; }
  .letterhead__footer {
    position: absolute; left: 0; bottom: 0; width: 100%; height: 36px;
    background: var(--navy);
    display: flex; align-items: center; gap: 34px; padding-left: 30px;
    font-size: 8.5px; color: #fff;
  }
  .letterhead__footer span { display: inline-flex; align-items: center; gap: 6px; }
  .footer-icon { width: 11px; height: 11px; border-radius: 50%; background: var(--blue-bright); }
</style>
</head>
<body>

<section class="signature">
  <div class="signature__photo" role="img" aria-label="Photo of an industrial refinery plant at dusk"></div>
  <div class="signature__band">
    <svg width="170" height="66" viewBox="0 0 170 66">
      <polygon points="70,0 110,0 70,66 30,66" fill="var(--blue)"/>
      <polygon points="118,0 170,0 170,66 78,66" fill="var(--blue-bright)"/>
      <polygon points="150,0 170,0 170,30" fill="var(--sky)"/>
    </svg>
  </div>
  <div class="signature__name">Declan Halloran</div>
  <div class="signature__role">Managing Director</div>

  <div class="signature__map" role="img" aria-label="Faint world map showing reseller locations"></div>

  <ul class="signature__contacts">
    <li><span class="contact-icon"><svg width="7" height="7" viewBox="0 0 10 10"><path d="M2 1l2 2-1 1.5c.8 1.5 1.5 2.2 3 3L7.5 6l2 2-1.5 1.5C4.5 9 1 5.5.5 2.5z" fill="#fff"/></svg></span>+61 412 508 733</li>
    <li><span class="contact-icon"><svg width="7" height="7" viewBox="0 0 10 10"><path d="M2 1l2 2-1 1.5c.8 1.5 1.5 2.2 3 3L7.5 6l2 2-1.5 1.5C4.5 9 1 5.5.5 2.5z" fill="#fff"/></svg></span>+08 9362 4170</li>
    <li><span class="contact-icon"><svg width="7" height="8" viewBox="0 0 10 12"><path d="M5 0a4 4 0 0 1 4 4c0 3-4 8-4 8S1 7 1 4a4 4 0 0 1 4-4z" fill="#fff"/></svg></span>42 Carden Street, Kewdale, WA 6105</li>
    <li><span class="contact-icon"><svg width="7" height="7" viewBox="0 0 10 10"><circle cx="5" cy="5" r="4" fill="none" stroke="#fff" stroke-width="1.2"/><line x1="1" y1="5" x2="9" y2="5" stroke="#fff"/></svg></span>www.brovantec.com.au</li>
  </ul>
  <div class="signature__social">
    <span class="social-dot"></span><span class="social-dot"></span><span class="social-dot"></span><span class="social-dot"></span>
  </div>

  <div class="brand"><span class="brand__dot"></span>Brovantec</div>

  <p class="signature__disclaimer">This email and any attachments are confidential and intended only for the named recipient. If you have received it in error, please notify the sender and delete it. Views expressed are those of the author and not necessarily of the company.</p>
</section>

<section class="letterhead">
  <svg class="letterhead__header-band" width="400" height="46" viewBox="0 0 400 46">
    <polygon points="40,8 400,8 400,40 24,40" fill="var(--navy)"/>
    <polygon points="250,8 330,8 314,40 234,40" fill="var(--blue)"/>
    <polygon points="340,0 400,0 400,46 318,46" fill="var(--blue-bright)"/>
  </svg>
  <div class="brand"><span class="brand__dot"></span>Brovantec</div>

  <div class="letterhead__map" role="img" aria-label="Faint map of Australia and surrounding region"></div>

  <div class="letterhead__body">
    <p>Dear Client,</p>
    <p>Thank you for your recent enquiry regarding our range of composite and convoluted hose. We are pleased to confirm that our Perth workshop can supply, test and certify each assembly to your stated pressure, temperature and media requirements, with full traceability documents provided on dispatch.</p>
    <p>Our engineering team has reviewed the drawings supplied for the plant shutdown and recommends metal expansion joints for the steam lines and fabric expansion joints for the exhaust ducting. Rubber expansion joints remain suitable for the slurry pump connections, provided the flange ratings are confirmed before manufacture begins.</p>
    <p>A detailed quotation, including lead times and freight to site, is attached for your review. Pricing is valid for thirty days from the date of this letter.</p>
    <p>Please do not hesitate to contact me should you require further information.</p>
    <p class="letterhead__signoff">Best Regards,</p>
  </div>

  <div class="letterhead__social">
    <span class="social-dot"></span><span class="social-dot"></span><span class="social-dot"></span><span class="social-dot"></span>
  </div>

  <footer class="letterhead__footer">
    <span><i class="footer-icon"></i>+61 412 508 733</span>
    <span><i class="footer-icon"></i>+08 9362 4170</span>
    <span><i class="footer-icon"></i>42 Carden Street, Kewdale, WA 6105</span>
    <span><i class="footer-icon"></i>www.brovantec.com.au</span>
  </footer>
</section>

</body>
</html>
```